Kelvo Tech Oz Business card revamp

We are looking to revamp our business card design. We are hoping to change our colours to dark navey blue, gray, white and black but are open to keeping the same if a good design is submited. We are after somthing a bit differnt not just boring business card. I have attached a copy of our current card. We Want to keep the same logo design which i have attached a few to hopfully help you in this process. We are after a design that can be personalized to separate 4 people

Colors
0455a3
ffffff
000000
cbcbcb

Requirements
Must have
• Kelvo Tech Logo, address 3/41 Mallory Court, Wexhill 4218, phone number, Name and position

```html
<!DOCTYPE html>
<html lang="en">
<head>
<meta charset="utf-8">
<title>Kelvo Tech Business Cards</title>
<link href="https://fonts.googleapis.com/css2?family=Open+Sans:wght@400;600;700&family=Ubuntu:wght@700&display=swap" rel="stylesheet">
<style>
  :root {
    --bg: #2b2b2d;
    --orange-light: #f9b233;
    --orange: #f36f21;
    --blue: #2f80c6;
    --blue-deep: #1f6fb8;
    --white: #ffffff;
    --brand-blue: #3a7fc4;
  }
  * { margin: 0; padding: 0; box-sizing: border-box; }
  html, body { width: 1200px; height: 900px; overflow: hidden; }
  body {
    background: var(--bg);
    font-family: "Open Sans", Arial, sans-serif;
    position: relative;
  }
  .card {
    position: absolute;
    left: 250px;
    width: 700px;
    height: 400px;
    overflow: hidden;
    box-shadow: 0 10px 30px rgba(0,0,0,0.45);
  }
  .card-front {
    top: 40px;
    background: linear-gradient(100deg, var(--orange-light) 0%, #f58a25 35%, var(--orange) 60%, var(--orange) 100%);
  }
  .card-back {
    top: 460px;
    background: var(--white);
  }
  .brand {
    display: flex;
    align-items: center;
    gap: 14px;
    font-family: "Ubuntu", Arial, sans-serif;
    font-weight: 700;
  }
  .brand-mark {
    width: 30px; height: 30px;
    border-radius: 50%;
  }
  .card-front .brand {
    position: absolute;
    left: 150px; top: 120px;
    font-size: 56px;
    color: var(--white);
  }
  .card-front .brand-mark { background: var(--white); }
  .services {
    position: absolute;
    left: 60px; right: 40px; top: 255px;
    color: var(--white);
    font-size: 17px;
    line-height: 1.45;
    text-align: center;
  }
  .back-wave { position: absolute; inset: 0; }
  .contact {
    position: absolute;
    right: 34px; top: 28px;
    text-align: right;
    color: var(--white);
    font-size: 16px;
    line-height: 1.45;
  }
  .contact-name { font-weight: 700; font-size: 17px; letter-spacing: 0.5px; }
  .contact-line { display: flex; justify-content: flex-end; align-items: center; gap: 8px; }
  .contact-line svg { width: 14px; height: 14px; fill: var(--white); }
  .card-back .brand {
    position: absolute;
    left: 190px; top: 290px;
    font-size: 50px;
    color: var(--brand-blue);
  }
  .card-back .brand-mark { background: var(--orange); }
</style>
</head>
<body>
  <section class="card card-front">
    <div class="brand"><span class="brand-mark"></span><span class="brand-name">Kelvo Tech</span></div>
    <p class="services">Service Penetrations • Steel Spray coatings • Intumescent paint<br>Boot Spray &amp; Wraps • Fire&amp;Smoke Barriers • Fire Rated Walls Ceilings</p>
  </section>

  <section class="card card-back">
    <svg class="back-wave" viewBox="0 0 700 400" preserveAspectRatio="none">
      <defs>
        <linearGradient id="waveBlue" x1="0" y1="0" x2="1" y2="1">
          <stop offset="0" stop-color="#3b8fd6"/>
          <stop offset="1" stop-color="#1f6fb8"/>
        </linearGradient>
      </defs>
      <path d="M0,0 H700 V250 C590,258 500,245 420,205 C330,160 250,100 150,100 C90,100 40,110 0,125 Z" fill="url(#waveBlue)"/>
      <path d="M150,112 C250,112 330,172 420,216 C500,256 590,266 700,258" fill="none" stroke="var(--orange)" stroke-width="5"/>
    </svg>
    <div class="contact">
      <p class="contact-name">DANA WHITLOW</p>
      <p>Director</p>
      <p>3/41 Mallory Court</p>
      <p>Wexhill 4218</p>
      <p class="contact-line">612 304 7781
        <svg viewBox="0 0 24 24"><path d="M6.6 10.8a15.1 15.1 0 0 0 6.6 6.6l2.2-2.2c.3-.3.7-.4 1-.2 1.1.4 2.3.6 3.6.6.6 0 1 .4 1 1V20c0 .6-.4 1-1 1C10.6 21 3 13.4 3 4c0-.6.4-1 1-1h3.5c.6 0 1 .4 1 1 0 1.3.2 2.5.6 3.6.1.3 0 .7-.2 1z"/></svg></p>
      <p class="contact-line">name@kelvotech.com.au
        <svg viewBox="0 0 24 24"><path d="M2 5h20v14H2z M3 6l9 7 9-7" stroke="#1f6fb8" stroke-width="1.5"/></svg></p>
      <p class="contact-line">www.kelvotech.com.au
        <svg viewBox="0 0 24 24"><circle cx="12" cy="12" r="10"/></svg></p>
    </div>
    <div class="brand"><span class="brand-mark"></span><span class="brand-name">Kelvo Tech</span></div>
  </section>
</body>
</html>
```